Brenmore Land Clearing postcard ( for direct mailing) and business card design

Design postcards/Business cards
Dale Hartwick
Brenmore Land Clearing
462 Quillstone Rd Lewisville,NC 27458
(336) 571-2846 Dale@Brenmorelandclearing.example

The postcard will be used for direct mailing to land owners and contractors to advertise our service. Pictures of the process and equipment along with a short summary of what we do. Business card should be contact info and logo.
Updates

The post cards could say something like this: Forestry Mulching machines are capable of clearing land of unwanted trees and brush with limited disturbance to soils or desirable vegetation. Traditional land clearing methods often present an increased risk of erosion by pushing over trees, uprooting the stump and roots, and substantially disturbing soils.In contrast, mulching the vegetation leaves the soil structure intact. The mulched material can be left on the ground and will act as an erosion barrier while returning nutrients back into the soil through decomposition. Over time, grass will naturally grow through the mulch and can be maintained with mowing.

Target Market(s)

Land owners and contractors who need vegetation cleared

Industry/Entity Type

Forestry Mulching

Requirements
Must have
• picture, brief description of service offered, contact info on postcard. Business card should have contact info and logo.
Nice to have
• I like contour lines as a background but I'd like to see other ideas.

```html
<!DOCTYPE html>
<html lang="en">
<head>
<meta charset="utf-8">
<title>Brenmore Land Clearing – Postcard</title>
<link href="https://fonts.googleapis.com/css2?family=Arimo:wght@400;700&display=swap" rel="stylesheet">
<style>
  :root {
    --forest: #1b7434;
    --leaf: #4cb848;
    --paper: #ffffff;
    --stage: #e6e6e6;
    --rule: #6f6f6f;
    --ink: #1e1e1e;
    --photo-dark: #2b2a20;
    --photo-mid: #4f5a4a;
    --photo-blue: #5a86b8;
  }
  html, body {
    margin: 0; padding: 0;
    width: 908px; height: 1200px;
    overflow: hidden;
    background: var(--stage);
    font-family: "Arimo", Arial, sans-serif;
  }
  .card {
    position: absolute;
    left: 184px;
    width: 380px; height: 380px;
    background: var(--paper);
    transform: scale(1.421);
    transform-origin: top left;
    overflow: hidden;
    box-shadow: 0 1px 3px rgba(0,0,0,.15);
  }
  .card--front { top: 30px; }
  .card--back { top: 630px; }
  .card svg.shapes { position: absolute; inset: 0; width: 380px; height: 380px; }

  .brand {
    position: absolute;
    display: flex; align-items: center; gap: 6px;
    font-weight: 700; color: var(--ink);
    letter-spacing: .4px; line-height: 1;
  }
  .brand__mark { width: 11px; height: 11px; background: var(--forest); flex: none; }
  .brand__name { width: 110px; font-size: 14px; }
  .card--front .brand { left: 24px; top: 24px; }
  .card--back .brand { left: 22px; top: 326px; }
  .card--back .brand__name { font-size: 11px; width: 90px; }

  .contact {
    position: absolute; right: 22px; top: 333px;
    color: var(--paper); font-size: 9px; line-height: 13px; text-align: right;
  }
  .contact__row { display: flex; justify-content: flex-end; align-items: center; gap: 10px; }
  .contact__row svg { width: 9px; height: 9px; }

  .summary {
    position: absolute; left: 22px; top: 22px; width: 335px;
    color: var(--paper); font-size: 8.5px; line-height: 10.6px;
    text-align: justify;
  }
  .summary p { margin: 0 0 10px; text-indent: 22px; }

  .address {
    position: absolute; left: 168px; top: 342px; width: 212px; height: 14px;
    background: var(--forest); color: var(--paper);
    font-size: 8.5px; line-height: 14px; text-align: center;
  }
</style>
</head>
<body>

<section class="card card--front" aria-label="Postcard front">
  <svg class="shapes" viewBox="0 0 380 380" aria-hidden="false">
    <defs>
      <linearGradient id="photoTone" x1="0" y1="0" x2="1" y2="1">
        <stop offset="0" stop-color="var(--photo-dark)"/>
        <stop offset=".5" stop-color="var(--photo-mid)"/>
        <stop offset=".75" stop-color="var(--photo-blue)"/>
        <stop offset="1" stop-color="#8a5a3a"/>
      </linearGradient>
    </defs>
    <polygon points="0,134 380,8 380,310 0,345" fill="url(#photoTone)" role="img" aria-label="Photo of a forestry mulching machine clearing brush in the woods"/>
    <polygon points="0,120 380,0 380,8 0,134" fill="var(--leaf)"/>
    <polygon points="0,340 380,300 380,380 0,380" fill="var(--forest)"/>
    <polygon points="0,340 380,300 380,304 0,345" fill="var(--leaf)"/>
    <polygon points="0,366 380,352 380,355 0,369" fill="var(--leaf)"/>
  </svg>
  <div class="brand"><span class="brand__mark"></span><span class="brand__name">Brenmore Land Clearing</span></div>
  <div class="contact">
    <div class="contact__row"><span>(336) 571-2846</span>
      <svg viewBox="0 0 10 10"><path d="M1 3 Q5 0 9 3 L8 4 L6 3 L4 3 L2 4 Z M2 5 H8 V9 H2 Z" fill="var(--leaf)"/></svg></div>
    <div class="contact__row"><span>Dale@Brenmorelandclearing.example</span>
      <svg viewBox="0 0 10 10"><rect x="1" y="2.5" width="8" height="5.5" fill="var(--leaf)"/><path d="M1 2.5 L5 6 L9 2.5" stroke="var(--forest)" fill="none" stroke-width=".8"/></svg></div>
  </div>
</section>

<section class="card card--back" aria-label="Postcard back">
  <svg class="shapes" viewBox="0 0 380 380" aria-hidden="true">
    <rect x="0" y="0" width="380" height="145" fill="var(--forest)"/>
    <rect x="0" y="145" width="380" height="3" fill="var(--leaf)"/>
    <g stroke="var(--rule)" stroke-width=".8">
      <line x1="22" y1="171" x2="357" y2="171"/>
      <line x1="22" y1="194" x2="357" y2="194"/>
      <line x1="22" y1="216" x2="357" y2="216"/>
      <line x1="22" y1="239" x2="357" y2="239"/>
      <line x1="22" y1="262" x2="357" y2="262"/>
      <line x1="22" y1="284" x2="357" y2="284"/>
      <line x1="22" y1="307" x2="357" y2="307"/>
    </g>
    <rect x="0" y="362" width="380" height="4" fill="var(--leaf)"/>
    <rect x="0" y="369" width="380" height="3" fill="var(--leaf)"/>
  </svg>
  <div class="summary">
    <p>Forestry Mulching is especially economical for smaller plots of land or areas with less access. When land needs to be cleared for adding roads, servicing pipelines, or creating recreational spaces in a wooded area, forestry mulching can be a very effective method of clearing spaces.</p>
    <p>Along with making space for planned projects, forestry mulching is also a great way to clear unwanted vegetation to allow more desirable food sources for local wildlife to flourish. Creating access to waterways that have become overgrown and clearing space for animals to gain new breeding grounds are other ways forestry mulching can be helpful.</p>
  </div>
  <div class="brand"><span class="brand__mark"></span><span class="brand__name">Brenmore Land Clearing</span></div>
  <div class="address">462 Quillstone Rd Lewisville,NC 27458</div>
</section>

</body>
</html>
```